Evenings at Calvera Playhouse Recital Season

Calvera Playhouse Recital Season

Febraury 1st - Peter Hale Brandt (Vesta Winner, Harbor Kids)
March 1st - Celia Dunworth (Silver Lantern Winner, The Fern)
April 5th - Marisol Pike (A Toast to Nina: The First Decade)
May 3rd - Teresa Galloway (Vesta Nominee, Polly)

All shows at 7:30PM

Subscribe to the series and save 10%

Get your tickets online at www.velbrookstages.com

Poster size 11" X 17" also 27" x 41"

Target Market(s)

Upscale market and music lovers. Small venue with international performers

Colors

Designer to choose colors to be used in the design.

Requirements
Must have
• Upscale - rich - style - like DIVA
Should not have
• Clip art

```html
<!DOCTYPE html>
<html lang="en">
<head>
<meta charset="utf-8">
<title>Calvera Playhouse Recital Season</title>
<link rel="stylesheet" href="https://fonts.googleapis.com/css2?family=Great+Vibes&family=Raleway:wght@200;300&display=swap">
<style>
  :root {
    --bg-deep: #070707;
    --bg-mid: #1c1c1c;
    --gold: #e3a54e;
    --silver: #e6e6e6;
    --caption: #c9c9c9;
    --accent-red: #d9382c;
  }
  html, body { margin: 0; padding: 0; overflow: hidden; background: var(--bg-deep); }
  .poster {
    position: relative;
    width: 790px; height: 1200px; overflow: hidden;
    background:
      radial-gradient(ellipse 70% 45% at 60% 55%, rgba(80,80,80,0.35), transparent 70%),
      linear-gradient(160deg, var(--bg-mid) 0%, var(--bg-deep) 55%, #111 100%);
    font-family: 'Raleway', sans-serif;
    color: var(--silver);
  }
  .sheen { position: absolute; inset: 0; }
  .title-script {
    position: absolute; top: 20px; left: 0; width: 100%;
    text-align: center; margin: 0;
    font-family: 'Great Vibes', cursive; font-weight: 400;
    font-size: 78px; color: var(--gold);
  }
  .title-caps {
    position: absolute; top: 150px; left: 0; width: 100%;
    text-align: center; margin: 0;
    font-weight: 200; font-size: 54px; letter-spacing: 9px;
  }
  .showtime {
    position: absolute; top: 232px; left: 0; width: 100%;
    text-align: center; margin: 0;
    font-weight: 300; font-size: 32px; letter-spacing: 4px;
  }
  .portrait {
    position: absolute; border-radius: 50%;
    box-shadow: 0 0 22px 6px rgba(255,255,255,0.18);
  }
  .performer { position: absolute; text-align: center; width: 460px; }
  .performer .date { font-weight: 300; font-size: 22px; letter-spacing: 3px; text-transform: uppercase; }
  .performer .name { font-family: 'Great Vibes', cursive; font-size: 44px; color: var(--gold); line-height: 1.1; margin: 4px 0 8px; }
  .performer .credit { font-weight: 300; font-size: 13px; letter-spacing: 1.5px; text-transform: uppercase; color: var(--caption); }
  .footer {
    position: absolute; top: 1062px; left: 0; width: 100%;
    text-align: center; color: var(--accent-red);
    font-weight: 300; font-size: 26px; line-height: 37px;
  }
  .footer p { margin: 0; }
</style>
</head>
<body>
<main class="poster">
  <svg class="sheen" width="790" height="1200" aria-hidden="true">
    <path d="M0 880 C250 700 520 760 790 560" fill="none" stroke="rgba(255,255,255,0.06)" stroke-width="2"/>
    <path d="M0 920 C260 760 540 800 790 620" fill="none" stroke="rgba(255,255,255,0.05)" stroke-width="2"/>
    <path d="M0 600 C300 470 520 520 790 300" fill="none" stroke="rgba(255,255,255,0.04)" stroke-width="2"/>
  </svg>

  <h1 class="title-script">Calvera Playhouse</h1>
  <h2 class="title-caps">RECITAL SEASON</h2>
  <p class="showtime">ALL SHOWS AT 7:30PM</p>

  <div class="portrait" role="img" aria-label="Portrait of Peter Hale Brandt"
       style="left:182px; top:333px; width:120px; height:140px; background:radial-gradient(circle at 50% 45%, #f2f2f2, #d8d8d8);"></div>
  <section class="performer" style="left:278px; top:344px;">
    <div class="date">Febraury 1st</div>
    <div class="name">Peter Hale Brandt</div>
    <div class="credit">(Vesta Winner, Harbor Kids)</div>
  </section>

  <div class="portrait" role="img" aria-label="Portrait of Celia Dunworth"
       style="left:516px; top:475px; width:130px; height:170px; background:radial-gradient(circle at 50% 40%, #8a8a8a, #2b2b2b);"></div>
  <section class="performer" style="left:100px; top:520px;">
    <div class="date">March 1st</div>
    <div class="name">Celia Dunworth</div>
    <div class="credit">(Silver Lantern Winner, The Fern)</div>
  </section>

  <div class="portrait" role="img" aria-label="Portrait of Marisol Pike"
       style="left:216px; top:666px; width:95px; height:140px; background:radial-gradient(circle at 50% 40%, #c0392b, #6b1a14);"></div>
  <section class="performer" style="left:356px; top:697px;">
    <div class="date">April 5th</div>
    <div class="name">Marisol Pike</div>
    <div class="credit">(A Toast to Nina: The First Decade)</div>
  </section>

  <div class="portrait" role="img" aria-label="Portrait of Teresa Galloway"
       style="left:517px; top:848px; width:120px; height:155px; background:radial-gradient(circle at 50% 40%, #e9c9c4, #b9848a);"></div>
  <section class="performer" style="left:90px; top:872px;">
    <div class="date">May 3rd</div>
    <div class="name">Teresa Galloway</div>
    <div class="credit">(Vesta Nominee, Polly)</div>
  </section>

  <footer class="footer">
    <p>Subscribe to the series and save 10%</p>
    <p>Get your tickets online at www.velbrookstages.com</p>
  </footer>
</main>
</body>
</html>
```